Beauty & Wellness business needs a flyer to describe a multitude of therapy

I would like a flyer to represent my company. i would like it to have the form of a pamphlet 6 pages. The flyer should be in french if possible, but english also is okay. I'll upload a word file that illustrate what i would like, but it can be of course other images, this is just an example. And the text includes all the services we provide, some small description might be added if you think it's worth it from design point of view.
Target Market(s)
The market is seasonal. it's mostly winter for skiers, so wealthy and sporty people, and attentive to nature. But i also want to promote the brand for locals all year long, with reasonable pricing.
Industry/Entity Type
Wellness & aesthetics
Look and feel

```html
<!DOCTYPE html>
<html lang="fr">
<head>
<meta charset="utf-8">
<title>Maëlle Studio – Dépliant Beauty &amp; Therapy</title>
<link href="https://fonts.googleapis.com/css2?family=Cormorant+Garamond:wght@500;600;700&family=Lora:wght@400;600&display=swap" rel="stylesheet">
<style>
  :root{
    --plum:#7a2a64;
    --plum-deep:#5e1d4c;
    --magenta:#a8477c;
    --blush:#f3dbe5;
    --blush-soft:#fbeef3;
    --ink:#4a3a44;
    --white:#ffffff;
    --page:#ffffff;
    --skin-light:#f6e4dc;
    --skin:#e3bfae;
    --skin-deep:#c99886;
  }
  *{box-sizing:border-box;margin:0;padding:0}
  html,body{width:853px;height:1200px;overflow:hidden;background:var(--page)}
  body{position:relative;font-family:"Lora",Georgia,serif;color:var(--ink)}
  .sheet{position:absolute;left:22px;width:808px;height:570px;display:grid;grid-template-columns:repeat(3,1fr);box-shadow:0 2px 8px rgba(0,0,0,.18);background:var(--white);overflow:hidden}
  .sheet--outside{top:15px}
  .sheet--inside{top:612px}
  .panel{position:relative;overflow:hidden;border-right:1px solid rgba(0,0,0,.05)}
  .panel:last-child{border-right:none}
  .photo{position:absolute}
  .body-text{font-size:8.2px;line-height:1.5}

  /* Outside – welcome panel */
  .welcome-bar{position:absolute;left:0;top:14px;width:215px;height:30px;background:var(--blush);border-radius:0 15px 15px 0;display:flex;align-items:center;padding-left:14px;font-family:"Cormorant Garamond",serif;font-weight:700;font-size:15px;color:var(--plum)}
  .welcome-mark{position:absolute;right:16px;top:14px;width:26px;height:26px;border:1.5px solid var(--magenta);border-radius:50%}
  .welcome-p1{position:absolute;left:14px;top:56px;width:240px}
  .welcome-p2{position:absolute;left:14px;top:160px;width:240px}
  .welcome-legs{left:14px;top:232px;width:104px;height:118px;border-radius:6px;background:linear-gradient(160deg,var(--skin-light),var(--skin) 60%,#f4e2e8)}
  .welcome-hands{left:150px;top:262px;width:104px;height:88px;border-radius:6px;background:linear-gradient(120deg,#f1d3d6,#dca8b6)}
  .welcome-foot{position:absolute;left:0;bottom:0;width:100%;height:210px}
  .welcome-p3{position:absolute;left:22px;bottom:48px;width:225px;color:var(--white);text-align:center}

  /* Outside – contact panel */
  .brand{position:absolute;left:0;top:40px;width:100%;text-align:center}
  .brand-dot{width:34px;height:34px;border-radius:50%;border:1.5px solid var(--magenta);margin:0 auto 8px}
  .brand-name{font-family:"Cormorant Garamond",serif;font-weight:700;font-size:19px;letter-spacing:2px;color:var(--plum)}
  .contact{position:absolute;left:0;top:116px;width:100%;text-align:center}
  .contact-lead{font-size:9.5px;line-height:1.4;margin-bottom:10px}
  .contact-line{display:flex;align-items:center;justify-content:center;gap:6px;font-size:11px;font-weight:600;color:var(--plum);margin-bottom:6px}
  .contact-line.small{font-size:8px;font-weight:400;color:var(--ink)}
  .contact-web{font-size:8.5px;margin-top:8px}
  .contact-web b{display:block;color:var(--plum);font-size:9px;margin-top:3px}
  .map{left:72px;top:262px;width:125px;height:125px;border-radius:50%;border:3px solid var(--blush);background:linear-gradient(135deg,#eef0ee,#dfe6e2 50%,#f4ecef)}
  .address{position:absolute;left:0;top:400px;width:100%;text-align:center;font-size:8.5px;line-height:1.5;letter-spacing:.5px}
  .contact-foot{position:absolute;left:0;bottom:0;width:100%;height:130px}
  .contact-web-foot{position:absolute;left:0;bottom:14px;width:100%;text-align:center;font-size:8px;color:var(--white)}

  /* Outside – cover panel */
  .cover-photo{left:0;top:0;width:100%;height:350px;background:linear-gradient(160deg,#f5ede8,var(--skin) 45%,var(--skin-deep) 75%,#f3e6e6)}
  .cover-band{position:absolute;left:0;top:350px;width:100%;height:220px;background:var(--plum)}
  .cover-wave{position:absolute;left:0;top:320px;width:100%;height:80px}
  .cover-title{position:absolute;right:20px;top:420px;font-family:"Cormorant Garamond",serif;font-weight:600;font-size:24px;color:var(--white)}
  .cover-web{position:absolute;right:22px;top:455px;font-size:8px;color:var(--white)}

  /* Inside */
  .section-head{position:absolute;left:0;height:22px;display:flex;align-items:center;padding-left:12px;font-family:"Cormorant Garamond",serif;font-weight:700;font-size:13px;color:var(--white);background:var(--plum);border-radius:0 12px 12px 0}
  .service-list{position:absolute;list-style:none;font-size:9px;line-height:1.62}
  .service-list li{display:flex;align-items:center;gap:6px}
  .service-list li::before{content:"";width:5px;height:5px;border-radius:50%;background:var(--magenta);flex:none}
  .service-list.on-dark{color:var(--white)}
  .service-list.on-dark li::before{background:var(--white)}

  .face-head{top:14px;width:190px}
  .face-list{left:14px;top:46px;width:130px}
  .face-photo-small{left:150px;top:44px;width:108px;height:132px;border-radius:6px;background:linear-gradient(150deg,#f7e5df,var(--skin) 60%,#f3dde3)}
  .wax-title{position:absolute;left:14px;top:200px;width:245px;font-family:"Cormorant Garamond",serif;font-weight:700;font-size:14px;line-height:1.3;color:var(--plum)}
  .face-photo{left:0;top:250px;width:100%;height:320px;background:linear-gradient(170deg,#fbf0ec,#efd5ca 45%,#dcb4a8 75%,#f4e4e9)}

  .massage-top{position:absolute;left:0;top:0;width:100%;height:300px;background:linear-gradient(180deg,var(--blush-soft),var(--blush))}
  .massage-head{top:14px;width:170px}
  .massage-list{left:14px;top:44px;width:140px}
  .massage-photo-a{left:150px;top:50px;width:105px;height:78px;border-radius:6px;background:linear-gradient(135deg,#e8d7cc,#c9a992)}
  .massage-photo-b{left:150px;top:140px;width:105px;height:78px;border-radius:6px;background:linear-gradient(135deg,#efe3d6,#b79f8a)}
  .massage-photo-c{left:0;top:300px;width:100%;height:160px;background:linear-gradient(160deg,#f2e2d8,#d9b4a2 55%,#b88674)}
  .massage-foot{position:absolute;left:0;top:440px;width:100%;height:130px}
  .massage-title{position:absolute;left:0;top:492px;width:100%;text-align:center;font-family:"Cormorant Garamond",serif;font-weight:600;font-size:24px;color:var(--white)}
  .massage-web{position:absolute;left:0;top:526px;width:100%;text-align:center;font-size:8px;color:var(--white)}

  .care-photo{left:0;top:0;width:100%;height:215px;background:linear-gradient(150deg,#f3dfd4,#d8ac94 50%,#a9705b)}
  .care-block{position:absolute;left:0;top:215px;width:100%;height:355px;background:linear-gradient(180deg,var(--plum),var(--plum-deep))}
  .care-wave{position:absolute;left:0;top:195px;width:100%;height:40px}
  .care-title{position:absolute;left:16px;font-family:"Cormorant Garamond",serif;font-weight:700;font-size:14px;color:var(--white)}
  .care-title.manicure{top:250px}
  .care-title.spa{top:350px}
  .care-list-a{left:18px;top:272px}
  .care-list-b{left:18px;top:372px}
  .care-photo-small{left:150px;top:248px;width:108px;height:92px;border-radius:50%;background:linear-gradient(135deg,#f5e3e6,#d9a9b8)}
  .care-photo-feet{left:150px;top:400px;width:108px;height:150px;border-radius:8px;background:linear-gradient(160deg,#f2e4dd,#d6b2a4)}
</style>
</head>
<body>

<section class="sheet sheet--outside">
  <article class="panel panel--welcome">
    <div class="welcome-bar">Welcome to Maëlle Studio</div>
    <div class="welcome-mark"></div>
    <p class="body-text welcome-p1">Je suis ravie de vous accueillir dans mon studio. Ici, chaque soin est pensé pour votre bien-être, avec des produits naturels et une attention sincère à vos besoins, été comme hiver. Mon approche associe des techniques douces et modernes pour révéler votre éclat naturel.</p>
    <p class="body-text welcome-p2">Après une journée sur les pistes, offrez à votre corps le repos qu'il mérite. Nos massages et soins du visage vous aident à récupérer en douceur et à retrouver énergie et sérénité.</p>
    <div class="photo welcome-legs" role="img" aria-label="Photo de jambes lisses après épilation"></div>
    <div class="photo welcome-hands" role="img" aria-label="Photo de mains manucurées"></div>
    <svg class="welcome-foot" viewBox="0 0 269 210" preserveAspectRatio="none" aria-hidden="true">
      <path d="M0 40 C90 0 180 10 269 50 L269 210 L0 210 Z" fill="var(--blush)"/>
      <path d="M0 58 C90 20 180 28 269 66 L269 210 L0 210 Z" fill="var(--plum)"/>
    </svg>
    <p class="body-text welcome-p3">Que vous soyez de passage pour la saison ou résident toute l'année, je vous propose des tarifs raisonnables et des soins adaptés à chacun.</p>
  </article>

  <article class="panel panel--contact">
    <div class="brand">
      <div class="brand-dot"></div>
      <div class="brand-name">MAËLLE STUDIO</div>
    </div>
    <div class="contact">
      <p class="contact-lead">Pour prendre un rendez-vous<br>ou une consultation gratuite:</p>
      <div class="contact-line">
        <svg width="12" height="12" viewBox="0 0 24 24" aria-hidden="true"><path fill="var(--plum)" d="M6.6 10.8a15.1 15.1 0 0 0 6.6 6.6l2.2-2.2a1 1 0 0 1 1-.25 11.4 11.4 0 0 0 3.6.57 1 1 0 0 1 1 1V20a1 1 0 0 1-1 1A17 17 0 0 1 3 4a1 1 0 0 1 1-1h3.5a1 1 0 0 1 1 1c0 1.25.2 2.45.57 3.57a1 1 0 0 1-.25 1z"/></svg>
        +41 79 000 1234
      </div>
      <div class="contact-line small">
        <svg width="10" height="10" viewBox="0 0 24 24" aria-hidden="true"><path fill="var(--plum)" d="M2 5h20v14H2zm2 2v.5l8 5 8-5V7z"/></svg>
        contact@maelle-studio.ch
      </div>
      <p class="contact-web">For more information, visit us at<b>www.maelle-studio.ch</b></p>
    </div>
    <div class="photo map" role="img" aria-label="Plan d'accès au studio"></div>
    <p class="address">ROUTE DES ALPES 12,<br>VERBIER, SUISSE</p>
    <svg class="contact-foot" viewBox="0 0 269 130" preserveAspectRatio="none" aria-hidden="true">
      <path d="M0 50 C80 10 180 60 269 20 L269 130 L0 130 Z" fill="var(--blush)"/>
      <path d="M0 72 C90 40 180 80 269 44 L269 130 L0 130 Z" fill="var(--plum)"/>
    </svg>
    <p class="contact-web-foot">www.maelle-studio.ch</p>
  </article>

  <article class="panel panel--cover">
    <div class="photo cover-photo" role="img" aria-label="Photo de trois femmes souriantes à la peau éclatante"></div>
    <div class="cover-band"></div>
    <svg class="cover-wave" viewBox="0 0 269 80" preserveAspectRatio="none" aria-hidden="true">
      <path d="M0 20 C90 50 180 0 269 25 L269 80 L0 80 Z" fill="var(--blush)"/>
      <path d="M0 42 C90 70 180 20 269 46 L269 80 L0 80 Z" fill="var(--plum)"/>
    </svg>
    <h1 class="cover-title">Beauty &amp; Therapy</h1>
    <p class="cover-web">www.maelle-studio.ch</p>
  </article>
</section>

<section class="sheet sheet--inside">
  <article class="panel panel--face">
    <h2 class="section-head face-head">Nos traitements du visage</h2>
    <ul class="service-list face-list">
      <li>Soin du visage classique</li>
      <li>Fils de collagènes</li>
      <li>Thérapie au pliée</li>
      <li>Plasma Lift</li>
      <li>Chromothérapie</li>
      <li>Aromathérapie</li>
      <li>Needling</li>
    </ul>
    <div class="photo face-photo-small" role="img" aria-label="Photo d'un soin du visage"></div>
    <h3 class="wax-title">Épilation masculine et Féminin<br>Design des sourcils</h3>
    <div class="photo face-photo" role="img" aria-label="Photo d'un visage au teint lumineux"></div>
  </article>

  <article class="panel panel--massage">
    <div class="massage-top"></div>
    <h2 class="section-head massage-head">Nos massages maisons</h2>
    <ul class="service-list massage-list">
      <li>Sportif</li>
      <li>Pierre chaude</li>
      <li>Ayurvédique Pindas</li>
      <li>Guasha</li>
      <li>Bamboo</li>
      <li>Drainage lymphatique</li>
      <li>Pour femmes enceintes</li>
      <li>Réflexologie</li>
      <li>Relaxant</li>
      <li>Shiatsu</li>
      <li>Deep tissue</li>
      <li>Minus Cellulite</li>
    </ul>
    <div class="photo massage-photo-a" role="img" aria-label="Photo de pierres chaudes"></div>
    <div class="photo massage-photo-b" role="img" aria-label="Photo de bâtons de bambou"></div>
    <div class="photo massage-photo-c" role="img" aria-label="Photo d'un massage du dos"></div>
    <svg class="massage-foot" viewBox="0 0 269 130" preserveAspectRatio="none" aria-hidden="true">
      <path d="M0 20 C90 60 180 0 269 30 L269 130 L0 130 Z" fill="var(--blush)"/>
      <path d="M0 38 C90 76 180 18 269 48 L269 130 L0 130 Z" fill="var(--plum)"/>
    </svg>
    <h2 class="massage-title">Beauty &amp; Therapy</h2>
    <p class="massage-web">www.maelle-studio.ch</p>
  </article>

  <article class="panel panel--care">
    <div class="photo care-photo" role="img" aria-label="Photo d'un massage relaxant"></div>
    <div class="care-block"></div>
    <svg class="care-wave" viewBox="0 0 269 40" preserveAspectRatio="none" aria-hidden="true">
      <path d="M0 20 C90 40 180 0 269 18 L269 40 L0 40 Z" fill="var(--plum)"/>
    </svg>
    <h3 class="care-title manicure">Manicure &amp; Pédicure</h3>
    <ul class="service-list on-dark care-list-a">
      <li>Semi permanent</li>
      <li>Gel</li>
      <li>Fibre de verre</li>
    </ul>
    <div class="photo care-photo-small" role="img" aria-label="Photo d'ongles vernis"></div>
    <h3 class="care-title spa">Spa des pieds</h3>
    <ul class="service-list on-dark care-list-b">
      <li>Algie thérapie</li>
      <li>Paraffine</li>
      <li>Plasma</li>
    </ul>
    <div class="photo care-photo-feet" role="img" aria-label="Photo d'un soin des pieds"></div>
  </article>
</section>

</body>
</html>
```